Venue Booking Site

I would like a venue directory and booking website designed. The idea is that end users will come to the site to find venues for weddings, parties, events etc. They will be able to find the venue based on many criteria, the most important ones are availability and location - they will be able to see in real time which venues are available for the desired dates and areas.

Venues will be able to use the website as a reservation management tool, receive payments for bookings through the site and be able to manage bookings on the go. This will be made into an app. It needs to be developed in bootstrap. Brand name to be used: Pinevault. Venue, place and space bookings.

Target audience - end users - anyone who is looking for a venue. For Community members it will provide an easy way to find a suitable venue
Outline what dates and times the venue is available
Outline costs involved in booking the venue
Search via many other criteria
It will allow the customer to book and pay for the venue online in one smooth process

Clients: Venue managers - particularly focussing on not for profit businesses eg, GPWs, community hall managers, small business managers. These people typically use paper based systems yet and do not use websites so it needs to be very user friendly. Future growth to restaurants, pubs, event venues who have a stronger familiarity with computers and who might already use their own booking management tool - so this needs to be able to link in with their system.

What need will this meet for venue managers:
This tool provides venues with greater visibility, promotion and advertising of their venue
This allows more customers to find them and book with them
This tool will be offered to not-for-profit venue managers for free to better connect them to the community
This means greater profit for these community venues
This means more revenue and jobs created in these communities

Sample of the layout / contents attached. This is not a complete site map as yet as it is a work in progress for final pages.

Industry/Entity Type

Small Business

Number of Pages Required

5+ page

Font styles to use
Sans Serif

Colors
eb2027

Requirements
Must have
• This is a psd file only - one template for each different section, home page, search page, detailed page view, admin back end
Should not have
• does not need to be coded.
• Note, the lantern quay logo jpeg files were files we were toying with using for this project- but I am happy to use the main pinevault logo- I will let you decide.

```html
<!DOCTYPE html>
<html lang="en">
<head>
<meta charset="utf-8">
<title>Pinevault – Venue Booking</title>
<link rel="stylesheet" href="https://fonts.googleapis.com/css2?family=Arimo:wght@400;700&display=swap">
<style>
:root{
  --red:#eb2027;
  --red-dark:#c8161d;
  --ink:#1a1a1a;
  --grey-text:#444;
  --cream:#f6f1e4;
  --field:#e9e4d6;
  --hero-dark:#3a3a36;
  --footer-dark:#2b2b2a;
  --white:#fff;
}
*{box-sizing:border-box;margin:0;padding:0}
html,body{width:1200px;height:2791px;overflow:hidden}
body{font-family:"Arimo",Arial,sans-serif;color:var(--ink);background:var(--white);position:relative}
.abs{position:absolute}

/* header */
.site-header{position:absolute;left:0;top:0;width:1200px;height:181px;background:var(--white)}
.brand{position:absolute;left:62px;top:28px;display:flex;align-items:center;gap:14px}
.brand-mark{width:22px;height:22px;background:var(--red)}
.brand-name{font-size:56px;font-weight:700;color:var(--red);letter-spacing:-1px;line-height:1}
.brand-tag{position:absolute;left:98px;top:126px;font-size:17px;font-weight:700;color:var(--ink);letter-spacing:.5px}
.support{position:absolute;right:86px;top:40px;text-align:right;font-size:15px;line-height:22px}
.support .num{display:flex;align-items:center;gap:6px;justify-content:flex-end}
.header-search{position:absolute;left:996px;top:108px;width:160px;height:22px;background:#c9c9c9;font-size:11px;color:#fff;padding:4px 8px}
.header-search svg{position:absolute;right:6px;top:4px}
.account-links{position:absolute;right:38px;top:148px;font-size:13px}

/* nav */
.main-nav{position:absolute;left:0;top:181px;width:1200px;height:45px;background:var(--red)}
.main-nav a{position:absolute;top:14px;color:var(--white);font-size:14px;font-weight:700;text-decoration:none}

/* hero */
.hero{position:absolute;left:0;top:226px;width:1200px;height:523px;background:linear-gradient(160deg,#55544c 0%,#3d3c37 45%,#2c2c29 100%)}
.hero-title{position:absolute;left:218px;top:196px;color:var(--white);font-size:27px;font-weight:700}
.hero-sub{position:absolute;left:238px;top:284px;width:400px;color:var(--white);font-size:20px;line-height:32px;text-align:center}
.search-panel{position:absolute;left:798px;top:55px;width:290px;height:417px;background:rgba(60,55,48,.82);padding-top:34px}
.search-panel h2{text-align:center;color:var(--white);font-size:14px;font-weight:700;margin-bottom:22px}
.field{width:226px;height:24px;margin:0 0 16px 40px;background:var(--field);font-size:11px;color:#555;padding:5px 8px;position:relative}
.field::after{content:"";position:absolute;right:6px;top:8px;border:6px solid transparent;border-top:8px solid #7b2320;border-bottom:0}
.search-btn{display:block;width:92px;height:26px;margin:12px auto 0;background:var(--red);color:var(--white);font-size:14px;font-weight:700;text-align:center;line-height:26px}
.map-view{text-align:center;color:var(--white);font-size:8px;font-weight:700;margin-top:10px;text-decoration:underline}

/* top venues */
.top-venues{position:absolute;left:0;top:758px;width:1200px;height:519px;background:var(--red);color:var(--white)}
.section-title{text-align:center;font-weight:700}
.top-venues .section-title{position:absolute;top:38px;width:100%;font-size:24px}
.top-venues .lead{position:absolute;top:90px;width:100%;text-align:center;font-size:16px}
.venue-card{position:absolute;top:138px;width:262px;background:var(--white);color:var(--ink)}
.venue-photo{height:214px;background:linear-gradient(180deg,#6a625a,#3c3834)}
.venue-name{position:absolute;top:92px;left:0;width:100%;height:46px;background:rgba(255,255,255,.85);display:flex;align-items:center;justify-content:center;text-align:center;font-size:14px;font-weight:700;padding:0 10px;line-height:17px}
.venue-foot{height:48px;display:flex;align-items:center;justify-content:center}
.venue-card.featured .venue-photo{height:200px}
.venue-info{display:flex;justify-content:space-between;padding:14px 18px 0;font-size:10px;line-height:16px}
.venue-info dl{display:grid;grid-template-columns:auto auto;column-gap:12px}
.view-btn{display:block;width:88px;height:26px;margin:10px auto 0;background:var(--red);color:var(--white);font-size:9px;font-weight:700;text-align:center;line-height:26px}
.view-all{position:absolute;right:38px;top:478px;font-size:14px;text-decoration:underline}

/* reasons */
.reasons-title{position:absolute;top:1332px;width:1200px;font-size:29px;font-weight:400;letter-spacing:.5px}
.reason{position:absolute;width:267px;height:248px;background:var(--cream);text-align:center;padding-top:22px}
.reason svg{display:block;margin:0 auto}
.reason h3{font-size:17px;font-weight:700;margin:12px 0 20px}
.reason p{font-size:13px;line-height:20px;color:var(--grey-text);padding:0 24px}
.reason.highlight{background:linear-gradient(160deg,#f0393f,#d8141b);color:var(--white)}
.reason.highlight p{color:var(--white)}

/* offers */
.offers{position:absolute;left:0;top:2067px;width:1200px;height:215px;background:var(--red);color:var(--white)}
.offers .section-title{position:absolute;top:44px;width:100%;font-size:27px}
.email-field{position:absolute;left:405px;top:109px;width:428px;height:38px;background:#bdbdbd;color:var(--white);font-size:15px;font-weight:700;text-align:center;line-height:38px}
.signup{position:absolute;top:170px;width:100%;text-align:center;font-size:17px;font-weight:700;text-decoration:underline}

/* footer */
.site-footer{position:absolute;left:0;top:2282px;width:1200px;height:509px;background:linear-gradient(180deg,#3a3a38,#222221);color:var(--white)}
.footer-brand{position:absolute;left:0;top:60px;width:100%;text-align:center}
.footer-brand .name{font-size:34px;font-weight:700;color:var(--red);line-height:1}
.footer-brand .tag{font-size:10px;font-weight:700;margin-top:4px}
.footer-col{position:absolute;top:180px;font-size:13px;line-height:25px}
.footer-col h4{font-size:14px;font-weight:700;margin-bottom:16px}
.support-list{line-height:22px}
.help-text{line-height:25px}
.social{position:absolute;left:72px;top:356px;display:flex;gap:18px}
.social span{width:15px;height:15px;border-radius:50%;background:var(--white);display:block}
.footer-bottom{position:absolute;left:72px;right:28px;top:466px;font-size:12px;display:flex;justify-content:space-between}
</style>
</head>
<body>

<header class="site-header">
  <div class="brand"><span class="brand-mark"></span><span class="brand-name">pinevault</span></div>
  <div class="brand-tag">VENUE BOOKING</div>
  <div class="support">
    <div>24/7 Support number</div>
    <div class="num"><svg width="12" height="14" viewBox="0 0 12 14"><path d="M2 1l3 0 1 3-2 1q1 3 4 5l1-2 3 1 0 3q-1 2-3 1Q2 10 1 3q0-2 1-2z" fill="#eb2027"/></svg>03 5550 1742</div>
  </div>
  <div class="header-search">Search entire site
    <svg width="14" height="14" viewBox="0 0 14 14"><circle cx="6" cy="6" r="4" stroke="#333" stroke-width="2" fill="none"/><path d="M9 9l4 4" stroke="#333" stroke-width="2"/></svg>
  </div>
  <div class="account-links">Sign in &nbsp;|&nbsp; Create an account</div>
</header>

<nav class="main-nav">
  <a style="left:58px">HOME</a>
  <a style="left:205px">VENUES</a>
  <a style="left:363px">NEWS &amp; OFFERS</a>
  <a style="left:510px">INSPIRATION</a>
  <a style="left:770px">SERVICES</a>
  <a style="left:940px">CONTACT</a>
  <a style="left:1107px">FAQS</a>
</nav>

<section class="hero" role="img" aria-label="Photo of a banquet hall set with white chairs and dining tables">
  <h1 class="hero-title">WELCOME TO PINEVAULT</h1>
  <p class="hero-sub">Pinevault helps you find and book your perfect event venue with ease.</p>
  <form class="search-panel">
    <h2>SEARCH YOUR PERFECT VENUE</h2>
    <div class="field">I'm looking for a venue for a</div>
    <div class="field">City</div>
    <div class="field">District</div>
    <div class="field">Date</div>
    <div class="field">Time</div>
    <div class="field">Num of people</div>
    <span class="search-btn">SEARCH</span>
    <div class="map-view">MAP VIEW</div>
  </form>
</section>

<section class="top-venues">
  <h2 class="section-title">TOP VENUES</h2>
  <p class="lead">Looking for some inspiration? We've created shortlists of the top venues.</p>

  <article class="venue-card featured" style="left:70px;height:314px">
    <div class="venue-photo" role="img" aria-label="Photo of an elegant function room with a piano"></div>
    <div class="venue-name">THE UPPER LOFT BY ASHGROVE EVENTS</div>
    <div class="venue-info">
      <div>Corporate,<br>Party<br>Wedding</div>
      <dl><dt>Capacity:</dt><dd>150</dd><dt>Virtual Tour:</dt><dd>Coming Soon</dd><dt>District:</dt><dd>Central</dd></dl>
    </div>
    <span class="view-btn">VIEW VENUE</span>
  </article>

  <article class="venue-card" style="left:337px">
    <div class="venue-photo" role="img" aria-label="Photo of a restaurant dining room"></div>
    <div class="venue-name">THE COPPER HEARTH</div>
    <div class="venue-foot"><svg width="20" height="14" viewBox="0 0 20 14"><path d="M2 2l8 8 8-8" stroke="#eb2027" stroke-width="4" fill="none"/></svg></div>
  </article>

  <article class="venue-card" style="left:605px">
    <div class="venue-photo" role="img" aria-label="Photo of a conference room with a long table" style="background:linear-gradient(180deg,#8a8f92,#3d4144)"></div>
    <div class="venue-name">Q LINKSPACE - CONFERENCE &amp; WORK ROOM</div>
    <div class="venue-foot"><svg width="20" height="14" viewBox="0 0 20 14"><path d="M2 2l8 8 8-8" stroke="#eb2027" stroke-width="4" fill="none"/></svg></div>
  </article>

  <article class="venue-card" style="left:872px">
    <div class="venue-photo" role="img" aria-label="Photo of a set dining table with flowers" style="background:linear-gradient(180deg,#b9aea0,#5a4a3e)"></div>
    <div class="venue-name">N KITCHEN</div>
    <div class="venue-foot"><svg width="20" height="14" viewBox="0 0 20 14"><path d="M2 2l8 8 8-8" stroke="#eb2027" stroke-width="4" fill="none"/></svg></div>
  </article>

  <span class="view-all">View All</span>
</section>

<h2 class="section-title reasons-title">WHY SHOULD YOU BOOK YOUR VENUE THROUGH PINEVAULT</h2>

<div class="reason highlight" style="left:26px;top:1412px" role="img" aria-label="Red tinted photo background">
  <svg width="46" height="50" viewBox="0 0 46 50"><circle cx="20" cy="14" r="11" fill="none" stroke="#fff" stroke-width="3"/><path d="M18 14v22l-5-4-3 3 10 12h16l4-14-6-4-8-1V14a2 2 0 0 0-8 0z" fill="#fff"/></svg>
  <h3>Handpicked Hotels</h3>
  <p>All Stayhaven venues ful fil strict selection criteria. Each hotel is chosen individually and inclusion cannot be bought</p>
</div>
<div class="reason" style="left:319px;top:1412px">
  <svg width="40" height="50" viewBox="0 0 40 50"><rect x="3" y="6" width="34" height="42" rx="3" fill="none" stroke="#333" stroke-width="3"/><rect x="12" y="2" width="16" height="8" rx="2" fill="#333"/><path d="M10 20h20M10 28h20M10 36h14" stroke="#333" stroke-width="3"/></svg>
  <h3>Detailed Descriptions</h3>
  <p>All Stayhaven venues ful fil strict selection criteria. Each hotel is chosen individually and inclusion cannot be bought</p>
</div>
<div class="reason" style="left:609px;top:1412px">
  <svg width="50" height="50" viewBox="0 0 50 50"><path d="M25 10a12 12 0 0 0-7 22v6h14v-6a12 12 0 0 0-7-22z" fill="none" stroke="#333" stroke-width="3"/><path d="M19 43h12M25 1v4M6 18h4M40 18h4M11 6l3 3M39 6l-3 3" stroke="#333" stroke-width="3"/></svg>
  <h3>Exclusive Knowledge</h3>
  <p>All Stayhaven venues ful fil strict selection criteria. Each hotel is chosen individually and inclusion cannot be bought</p>
</div>
<div class="reason" style="left:902px;top:1412px">
  <svg width="50" height="50" viewBox="0 0 50 50"><circle cx="20" cy="13" r="10" fill="#333"/><path d="M2 48q0-22 18-22t18 22z" fill="#333"/><path d="M30 38l6 6 12-14" stroke="#333" stroke-width="4" fill="none"/></svg>
  <h3>Passionate Service</h3>
  <p>All Stayhaven venues ful fil strict selection criteria. Each hotel is chosen individually and inclusion cannot be bought</p>
</div>

<div class="reason" style="left:26px;top:1737px">
  <svg width="48" height="50" viewBox="0 0 48 50"><rect x="2" y="22" width="10" height="24" fill="#333"/><path d="M15 22l10-18q5 0 4 8l-2 8h15q4 1 3 5l-4 18q-1 3-4 3H15z" fill="#333"/></svg>
  <h3>Best Price Guarantee</h3>
  <p>All Stayhaven venues ful fil strict selection criteria. Each hotel is chosen individually and inclusion cannot be bought</p>
</div>
<div class="reason" style="left:319px;top:1737px">
  <svg width="40" height="50" viewBox="0 0 40 50"><path d="M10 22v-8a10 10 0 0 1 20 0v8" fill="none" stroke="#333" stroke-width="4"/><rect x="3" y="22" width="34" height="26" rx="4" fill="#333"/><circle cx="20" cy="33" r="4" fill="#f6f1e4"/></svg>
  <h3>Secure Booking</h3>
  <p>All Stayhaven venues ful fil strict selection criteria. Each hotel is chosen individually and inclusion cannot be bought</p>
</div>
<div class="reason" style="left:609px;top:1737px">
  <svg width="50" height="50" viewBox="0 0 50 50"><circle cx="22" cy="18" r="15" fill="none" stroke="#333" stroke-width="3"/><path d="M22 10v16M17 14h8M17 22h8" stroke="#333" stroke-width="2"/><rect x="24" y="34" width="22" height="5" rx="2" fill="#333"/><rect x="24" y="41" width="22" height="5" rx="2" fill="#333"/></svg>
  <h3>Benefits for Hoteliers</h3>
  <p>All Stayhaven venues ful fil strict selection criteria. Each hotel is chosen individually and inclusion cannot be bought</p>
</div>
<div class="reason" style="left:902px;top:1737px">
  <svg width="36" height="50" viewBox="0 0 36 50"><path d="M6 14a12 12 0 1 1 18 10q-6 4-6 12" fill="none" stroke="#333" stroke-width="6"/><rect x="14" y="41" width="8" height="8" fill="#333"/></svg>
  <h3>Any Questions?</h3>
  <p>All Stayhaven venues ful fil strict selection criteria. Each hotel is chosen individually and inclusion cannot be bought</p>
</div>

<section class="offers">
  <h2 class="section-title">DON'T MISS OUR EXCLUSIVE OFFERS</h2>
  <div class="email-field">ENTER EMAIL ID</div>
  <div class="signup">SING UP</div>
</section>

<footer class="site-footer" role="img" aria-label="Faint street map background">
  <div class="footer-brand"><div class="name">pinevault</div><div class="tag">VENUE BOOKING</div></div>

  <div class="footer-col" style="left:72px">
    <h4>PINEVAULT BOOKINGS</h4>
    <div>12 Harlow Lane Eastbrook VIC</div>
    <div>P: 03 5550 1749</div>
    <div>E: info@bookings.pinevault.example</div>
  </div>

  <div class="footer-col support-list" style="left:481px">
    <h4>CUSTOMER SUPPORT</h4>
    <div>Faq</div>
    <div>How do I make a reservation?</div>
    <div>Payment options</div>
    <div>Booking tips</div>
  </div>

  <div class="footer-col help-text" style="left:812px;top:170px">
    <div>Never Booked an Event Before?</div>
    <div>Having trouble getting started? That's okay!</div>
    <div>We are here to help, contact us by email,</div>
    <div>or give us a call and we will guide you through it.</div>
  </div>
  <svg class="abs" style="left:906px;top:318px" width="36" height="26" viewBox="0 0 36 26"><rect x="2" y="2" width="32" height="22" fill="none" stroke="#eb2027" stroke-width="3"/><path d="M2 2l16 13 16-13" fill="none" stroke="#eb2027" stroke-width="3"/></svg>
  <svg class="abs" style="left:982px;top:312px" width="20" height="34" viewBox="0 0 20 34"><rect x="2" y="2" width="16" height="30" rx="3" fill="none" stroke="#eb2027" stroke-width="3"/><path d="M2 8h16M2 25h16" stroke="#eb2027" stroke-width="2"/></svg>

  <div class="social"><span></span><span></span><span></span><span></span><span></span><span></span><span></span><span></span></div>

  <div class="footer-bottom">
    <span>© 2014 Copyright Pinevault</span>
    <span>About us &nbsp;|&nbsp; Contact &nbsp;|&nbsp; Partners &nbsp;|&nbsp; Customer service &nbsp;|&nbsp; FAQ &nbsp;|&nbsp; Careers &nbsp;|&nbsp; Terms &amp; Conditions &nbsp;|&nbsp; Privacy statement</span>
  </div>
</footer>

</body>
</html>
```